LUMETTE INC. is a new Fashion Stylist, Design Merchandiser, and consultant in the fashion industry

We need a logo design for a new Calgary, Alberta based company that is in the business of making over your image, wardrobe and style for both business and personal purposes.

Target Market(s)

Professional female and male business people looking for a new style or complete fashion makeover including clothes closet merchandising and makeover.

Contact Information for Business Card

see the uploaded file

Number of Pages Required

1 page

Font styles to use
Script

Colors
fac994
fbe7d2
fee3d4

Requirements
Must have
• Fashion Industry theme that is very elegant and colorful using gold/bronze/silver color themes.
Nice to have
• Incorporate the company name with the creative font to come up with the appropriate "logo"

```html
<!DOCTYPE html>
<html lang="en">
<head>
<meta charset="utf-8">
<title>Lumette Inc. — Business Card</title>
<link rel="stylesheet" href="https://fonts.googleapis.com/css2?family=Questrial&display=swap">
<style>
  :root {
    --backdrop: #d1d2d4;
    --card: #000000;
    --gold: #fac994;
    --cream: #fbe7d2;
    --silver: #e6e6e6;
  }
  * { margin: 0; padding: 0; box-sizing: border-box; }
  html, body {
    width: 1200px;
    height: 936px;
    overflow: hidden;
    background: var(--backdrop);
    font-family: "Questrial", "Helvetica Neue", Arial, sans-serif;
  }
  .sheet {
    position: relative;
    width: 1200px;
    height: 936px;
  }
  .card {
    position: absolute;
    left: 229px;
    width: 682px;
    height: 389px;
    background: var(--card);
    border-radius: 16px;
  }
  .card--front { top: 42px; }
  .card--back { top: 484px; }

  .brand-name {
    position: absolute;
    left: 0;
    right: 0;
    text-align: center;
    color: var(--cream);
    font-size: 40px;
    font-weight: 400;
    letter-spacing: 1px;
    line-height: 1;
  }
  .card--front .brand-name { top: 102px; left: 6px; }
  .card--back .brand-name { top: 172px; left: -12px; }

  .contact {
    position: absolute;
    left: 0;
    right: 0;
    top: 236px;
    text-align: center;
  }
  .contact__name {
    color: var(--gold);
    font-size: 27px;
    letter-spacing: -1px;
    line-height: 1;
  }
  .contact__role {
    margin-top: 13px;
    color: var(--gold);
    font-size: 17px;
    font-style: italic;
    letter-spacing: 1.6px;
    word-spacing: 3px;
    line-height: 1;
  }
  .contact__phone {
    margin-top: 19px;
    color: var(--silver);
    font-size: 17px;
    font-style: italic;
    letter-spacing: 1.8px;
    line-height: 1;
  }
</style>
</head>
<body>
  <main class="sheet">
    <section class="card card--front">
      <div class="brand-name">LUMETTE INC.</div>
      <div class="contact">
        <p class="contact__name">ELISE MARVANNE</p>
        <p class="contact__role">fashion stylist design merchandiser consultant</p>
        <p class="contact__phone">555-014-2297</p>
      </div>
    </section>
    <section class="card card--back">
      <div class="brand-name">LUMETTE INC.</div>
    </section>
  </main>
</body>
</html>
```